Brindle Paw & Pet Haulage

We need a new business card for a new business. We transport animals mainly dogs specialising in greyhounds travelling locally and interstate in air conditioned comfort. The design should incorporate the australian flag

Reason: just want to get the right design

Industry/Entity Type

Business

```html
<!DOCTYPE html>
<html lang="en">
<head>
<meta charset="utf-8">
<title>Brindle Paw &amp; Pet Haulage – Business Card</title>
<link rel="stylesheet" href="https://fonts.googleapis.com/css2?family=Open+Sans:wght@400;600&display=swap">
<style>
  :root {
    --page-bg: #e6e6e6;
    --card-white: #ffffff;
    --card-grey: #4f4e50;
    --brand-blue: #233e8b;
    --text-light: #ffffff;
  }
  html, body {
    margin: 0;
    padding: 0;
    width: 1200px;
    height: 985px;
    overflow: hidden;
    background: var(--page-bg);
    font-family: "Open Sans", Arial, sans-serif;
  }
  .business-card {
    position: absolute;
    left: 180px;
    top: 252px;
    width: 840px;
    height: 480px;
    border-radius: 28px;
    overflow: hidden;
    background: var(--card-white);
    box-shadow: 0 6px 18px rgba(0, 0, 0, 0.18);
  }
  .card-curves {
    position: absolute;
    inset: 0;
  }
  .brand-block {
    position: absolute;
    left: 70px;
    top: 150px;
    width: 290px;
    display: flex;
    align-items: center;
    gap: 16px;
  }
  .brand-dot {
    flex: none;
    width: 44px;
    height: 44px;
    border-radius: 50%;
    background: var(--brand-blue);
  }
  .brand-name {
    margin: 0;
    font-size: 28px;
    line-height: 1.2;
    font-weight: 600;
    color: var(--brand-blue);
  }
  .contact-block {
    position: absolute;
    left: 500px;
    top: 180px;
    color: var(--text-light);
  }
  .contact-name {
    margin: 0 0 6px;
    font-size: 32px;
    font-weight: 400;
    color: var(--brand-blue);
    letter-spacing: 0.5px;
  }
  .contact-line {
    margin: 0;
    font-size: 26px;
    line-height: 1.2;
    letter-spacing: 0.5px;
  }
</style>
</head>
<body>
  <div class="business-card">
    <svg class="card-curves" width="840" height="480" viewBox="0 0 840 480" aria-hidden="true">
      <path class="curve-band" fill="var(--brand-blue)" d="M488,0 C350,70 290,260 342,480 L840,480 L840,0 Z"/>
      <path class="curve-panel" fill="var(--card-grey)" d="M545,0 C395,75 318,265 364,480 L840,480 L840,0 Z"/>
    </svg>

    <div class="brand-block">
      <span class="brand-dot"></span>
      <p class="brand-name">Brindle Paw &amp; Pet Haulage</p>
    </div>

    <div class="contact-block">
      <p class="contact-name">Mara Lindqvist</p>
      <p class="contact-line">0491 570 113</p>
      <p class="contact-line">Website - TBA</p>
      <p class="contact-line">ABN 51824753556</p>
    </div>
  </div>
</body>
</html>
```